Pelorin Conference

We need a pullup banner 23x63 inches. We are attaching an example of a draft that we created. Can you please make it look more professional?
Thank you!

```html
<!DOCTYPE html>
<html lang="en">
<head>
<meta charset="utf-8">
<title>Isobar Climate – Pull-up Banner</title>
<link rel="stylesheet" href="https://fonts.googleapis.com/css2?family=Sora:wght@700;800&family=Lexend:wght@500&family=Roboto+Condensed:wght@700&display=swap">
<style>
  :root {
    --stage: #5b5b5b;
    --navy: #1f2a63;
    --orange: #f39c36;
    --orange-line: #c9741f;
    --brown: #9a7560;
    --deep-blue: #1b3a7e;
    --mid-blue: #1d6cb5;
    --sky: #2a98d0;
    --sky-light: #a9d6ea;
    --panel-blue: #27386f;
    --white: #ffffff;
    --grey-text: #7a7a7a;
  }
  * { margin: 0; padding: 0; box-sizing: border-box; }
  html, body { width: 711px; height: 1200px; overflow: hidden; background: var(--stage); }
  .banner {
    position: absolute; top: 0; left: 136px;
    width: 438px; height: 1200px; overflow: hidden; background: var(--white);
  }

  .brand {
    position: absolute; top: 68px; left: 0; right: 0;
    display: flex; align-items: center; justify-content: center; gap: 16px;
  }
  .brand-dot { width: 70px; height: 70px; border-radius: 50%; background: var(--orange); }
  .brand-name {
    font-family: "Sora", sans-serif; font-weight: 800; font-size: 22px;
    line-height: 1.15; color: var(--navy); letter-spacing: 0.3px;
  }

  .hero {
    position: absolute; top: 153px; left: 0; width: 438px; height: 784px;
    background: linear-gradient(180deg,
      var(--orange) 0%, var(--orange) 9%, var(--brown) 16%,
      var(--deep-blue) 28%, var(--mid-blue) 38%, var(--sky) 53%,
      var(--sky-light) 84%, var(--panel-blue) 91%, var(--panel-blue) 100%);
  }
  .hero-wave { position: absolute; top: 0; left: 0; width: 438px; height: 92px; }
  .hero-photo { position: absolute; left: 0; bottom: 0; width: 438px; height: 446px; }
  .headline {
    position: absolute; top: 119px; left: 0; right: 0; text-align: center;
    font-family: "Sora", sans-serif; font-weight: 700; font-size: 52px;
    line-height: 1.12; color: var(--white); letter-spacing: -0.5px;
  }

  .services {
    position: absolute; top: 937px; left: 0; width: 438px; height: 188px;
    background: var(--orange); padding: 19px 19px 20px;
  }
  .services-grid {
    display: grid; grid-template-columns: 185px 1fr; grid-template-rows: 1fr 1fr 1fr;
    height: 100%; border: 1.5px solid var(--orange-line);
  }
  .service {
    display: flex; align-items: center; gap: 10px; padding-left: 10px;
    border-bottom: 1.5px solid var(--orange-line);
    font-family: "Lexend", sans-serif; font-weight: 500; font-size: 16.5px;
    color: var(--white); letter-spacing: 0.2px; white-space: nowrap;
  }
  .service:nth-child(odd) { border-right: 1.5px solid var(--orange-line); }
  .service.full { grid-column: 1 / 3; justify-content: center; border-right: none; border-bottom: none; padding-left: 0; }
  .service-icon {
    width: 34px; height: 34px; border-radius: 50%; background: var(--white);
    display: flex; align-items: center; justify-content: center; flex: none;
  }
  .service-icon svg { width: 20px; height: 20px; fill: none; stroke: var(--orange-line); stroke-width: 1.6; }

  .contact {
    position: absolute; top: 1125px; left: 0; width: 438px; height: 75px;
    display: flex; flex-direction: column; align-items: center; justify-content: center;
    font-family: "Roboto Condensed", sans-serif; font-weight: 700; color: var(--grey-text);
    line-height: 1.05;
  }
  .contact-email { font-size: 26px; }
  .contact-web { font-size: 24px; }
</style>
</head>
<body>
<main class="banner">
  <header class="brand">
    <span class="brand-dot"></span>
    <span class="brand-name">ISOBAR<br>CLIMATE</span>
  </header>

  <section class="hero">
    <div class="hero-photo" role="img" aria-label="Photo of wind turbines against a blue sky with clouds, solar panels in the foreground"></div>
    <svg class="hero-wave" viewBox="0 0 438 92" preserveAspectRatio="none" aria-hidden="true">
      <path d="M0 0 H438 V0 C400 60 360 92 318 90 C250 88 180 24 110 26 C60 28 25 50 0 73 Z" fill="#ffffff"/>
    </svg>
    <h1 class="headline">Scaling the<br>Market for<br>Climate Risk<br>Transfer</h1>
  </section>

  <section class="services">
    <div class="services-grid">
      <div class="service">
        <span class="service-icon"><svg viewBox="0 0 24 24"><circle cx="12" cy="8" r="4"/><path d="M4 21c0-5 3.5-7 8-7s8 2 8 7"/></svg></span>ADVISORY
      </div>
      <div class="service">
        <span class="service-icon"><svg viewBox="0 0 24 24"><rect x="9" y="2" width="6" height="5"/><rect x="2" y="16" width="5" height="5"/><rect x="9.5" y="16" width="5" height="5"/><rect x="17" y="16" width="5" height="5"/><path d="M12 7v5M4.5 16v-4h15v4M12 12v4"/></svg></span>STRUCTURING
      </div>
      <div class="service">
        <span class="service-icon"><svg viewBox="0 0 24 24"><path d="M12 21s-6-6-6-11a6 6 0 0 1 12 0c0 5-6 11-6 11z"/><circle cx="12" cy="10" r="2.2"/></svg></span>PLACEMENT
      </div>
      <div class="service">
        <span class="service-icon"><svg viewBox="0 0 24 24"><rect x="4" y="3" width="12" height="18"/><path d="M7 8h6M7 12h6M7 16h3M13 18l8-8"/></svg></span>UNDERWRITING
      </div>
      <div class="service full">
        <span class="service-icon"><svg viewBox="0 0 24 24"><rect x="3" y="3" width="18" height="18"/><path d="M7 17v-3M11 17v-6M15 17v-4M18 17V8"/></svg></span>ANALYTICS
      </div>
    </div>
  </section>

  <footer class="contact">
    <span class="contact-email">contact@isobarclimate.com</span>
    <span class="contact-web">isobarclimate.com</span>
  </footer>
</main>
</body>
</html>
```